KRV e-payment Business Card Design

We require a new business card design to suit our expanding consulting business -who are specialists in 2 main areas
1. Advising large Corporations and Government organisation on how to improve the why they use emerging (B2B) electronic payment systems
2. Educate Global and regional banks on how to design, build and market electronic business payment products in emerging markets

Our logo is grey/silver based with a building block theme. It also suggests "insight" and business know-how capitalizing on our KRV name. We also want to engender trust,security and balance via the ying/yan symbol

The design needs to take into account the target regional areas of Australiasia/Asia Pacific/Middle East and Africa

Target Market(s)

Regional Banks and their business customers

Industry/Entity Type

Electronic

Contact Information for Business Card

Marcus Delwyn
Director KRV Consulting (Aust) Pty Ltd
PO Box 7463
Brookvale NSW 2175
Australia
tel +61 (0) 2 95550417
mob +61 (0) 455503862
krvconsulting@tallwire.example

```html
<!DOCTYPE html>
<html lang="en">
<head>
<meta charset="utf-8">
<title>KRV e-payment Business Card</title>
<link href="https://fonts.googleapis.com/css2?family=Questrial&family=Tinos:wght@400;700&display=swap" rel="stylesheet">
<style>
  :root {
    --page: #ffffff;
    --ink-dark: #0d0d0d;
    --card-black: #151515;
    --card-black-2: #262626;
    --silver-light: #f4f4f4;
    --silver-mid: #d9d9d9;
    --silver-band: #8a8a8a;
    --text-light: #e6e6e6;
    --text-muted: #9a9a9a;
    --text-dark: #222222;
    --accent-rule: #5a1e1e;
  }
  html, body {
    margin: 0;
    padding: 0;
    width: 1200px;
    height: 900px;
    overflow: hidden;
    background: var(--page);
  }
  .canvas {
    position: relative;
    width: 1200px;
    height: 900px;
    display: flex;
    align-items: center;
    justify-content: center;
    gap: 64px;
  }
  .card {
    position: relative;
    width: 500px;
    height: 300px;
    border-radius: 24px;
    overflow: hidden;
    box-shadow: 0 18px 30px rgba(0,0,0,0.18);
  }

  /* Front */
  .card--front {
    background: radial-gradient(ellipse at 60% 30%, var(--card-black-2), var(--card-black) 70%);
  }
  .front__emblem {
    position: absolute;
    left: 140px;
    top: 10px;
    width: 280px;
    height: 280px;
    border-radius: 50%;
    background: radial-gradient(circle, rgba(255,255,255,0.10), rgba(255,255,255,0.04) 70%);
  }
  .front__tagline {
    position: absolute;
    left: 40px;
    top: 126px;
    margin: 0;
    font-family: "Questrial", sans-serif;
    font-size: 21px;
    letter-spacing: 0.22em;
    color: var(--text-light);
    white-space: nowrap;
  }
  .front__brand {
    position: absolute;
    left: 230px;
    top: 196px;
  }

  /* Brand lockup */
  .brand {
    display: flex;
    align-items: center;
    gap: 10px;
  }
  .brand__square {
    width: 14px;
    height: 14px;
    border: 1.5px solid currentColor;
  }
  .brand__name {
    font-family: "Tinos", serif;
    font-weight: 700;
    white-space: nowrap;
  }
  .brand--light { color: var(--text-light); }
  .brand--light .brand__name { font-size: 22px; }
  .brand--dark { color: var(--text-dark); }
  .brand--dark .brand__name { font-size: 24px; }
  .brand__sub {
    display: block;
    font-size: 12px;
    font-weight: 700;
    letter-spacing: 0.02em;
  }

  /* Back */
  .card--back {
    background: linear-gradient(180deg, var(--silver-light) 0%, #ffffff 35%, var(--silver-mid) 58%);
  }
  .back__person {
    position: absolute;
    right: 26px;
    top: 36px;
    text-align: right;
    font-family: "Tinos", serif;
    color: var(--text-dark);
  }
  .back__name {
    margin: 0;
    font-size: 15px;
    font-weight: 700;
  }
  .back__role {
    margin: 2px 0 0;
    font-size: 12px;
    color: #555;
  }
  .back__brand {
    position: absolute;
    left: 34px;
    top: 74px;
  }
  .back__band {
    position: absolute;
    left: 0;
    right: 0;
    top: 160px;
    height: 18px;
    background: linear-gradient(90deg, #c8c8c8, var(--silver-band) 55%, #b5b5b5);
    display: flex;
    align-items: center;
    justify-content: flex-end;
    padding-right: 40px;
    font-family: "Questrial", sans-serif;
    font-size: 13px;
    letter-spacing: 0.3em;
    font-weight: 700;
    color: var(--ink-dark);
  }
  .back__contact {
    position: absolute;
    left: 0;
    right: 0;
    top: 178px;
    bottom: 0;
    background: linear-gradient(180deg, #1d1d1d, var(--card-black));
    padding: 16px 0 0 34px;
    box-sizing: border-box;
    font-family: "Tinos", serif;
    font-size: 14px;
    line-height: 1.2;
    color: var(--text-light);
  }
  .contact__line { margin: 0; }
  .contact__label { display: inline-block; width: 34px; }
  .contact__value { font-weight: 700; }
</style>
</head>
<body>
  <main class="canvas">
    <section class="card card--front" aria-label="Business card front">
      <div class="front__emblem" role="img" aria-label="Faint balance emblem decoration"></div>
      <p class="front__tagline">“real e-payment insight”</p>
      <div class="front__brand brand brand--light">
        <span class="brand__square"></span>
        <span class="brand__name">KRV <span class="brand__sub">Consulting (Australia) Pty Ltd</span></span>
      </div>
    </section>

    <section class="card card--back" aria-label="Business card back">
      <div class="back__person">
        <p class="back__name">Marcus Delwyn</p>
        <p class="back__role">Director</p>
      </div>
      <div class="back__brand brand brand--dark">
        <span class="brand__square"></span>
        <span class="brand__name">KRV <span class="brand__sub">Consulting (Australia) Pty Ltd</span></span>
      </div>
      <div class="back__band">“real e-payment insight”</div>
      <div class="back__contact">
        <p class="contact__line"><span class="contact__label">tel</span>: <span class="contact__value">+61 (0) 2 95550417</span></p>
        <p class="contact__line"><span class="contact__label">mob</span>: <span class="contact__value">+61 (0) 455503862</span></p>
        <p class="contact__line">krvconsulting@tallwire.example</p>
        <p class="contact__line">KRV Consulting (Aust) Pty Ltd PO Box 7463</p>
        <p class="contact__line">Brookvale NSW 2175 Australia</p>
      </div>
    </section>
  </main>
</body>
</html>
```